TRL Vetting Background Check Company

TRL Vetting is an eCommerce background check company offering three services payable online. The Candidate Review Unit is a team of skilled, experienced investigators who regularly conduct fact-findings (many daily) on federal, state, and local background checks.

Target Market(s)

All businesses that hire employees, as well as domestic persons that have a need for nannies, housekeepers and handymen. Persons in the dating community will utilize the services also.

Coding

Coded - Design and coding required

Font styles to use
Sans Serif

```html
<!DOCTYPE html>
<html lang="en">
<head>
<meta charset="utf-8">
<title>TRL Vetting — Background Checks</title>
<link href="https://fonts.googleapis.com/css2?family=Ubuntu:wght@400;500;700&family=Open+Sans:wght@400;600;700&display=swap" rel="stylesheet">
<style>
:root{
  --navy:#13285e;
  --red:#c0192c;
  --blue:#1565c0;
  --light:#f3f5fa;
  --ink:#222;
  --muted:#7a7f8c;
  --footer:#1c1630;
  --white:#fff;
}
*{box-sizing:border-box;margin:0;padding:0}
html,body{width:1200px;height:4249px;overflow:hidden}
body{position:relative;font-family:"Open Sans",sans-serif;color:var(--ink);background:var(--white)}
.abs{position:absolute}
h1,h2,h3,.brand{font-family:"Ubuntu",sans-serif}
.photo{position:absolute}

/* header */
.site-header{position:absolute;left:0;top:0;width:1200px;height:87px;background:#fff;border-top:3px solid var(--blue);z-index:3}
.brand{position:absolute;left:180px;top:26px;font-size:30px;font-weight:700;color:var(--navy);display:flex;align-items:center;gap:10px}
.brand .dot{width:22px;height:22px;border-radius:50%;background:var(--red)}
.nav{position:absolute;top:49px;font-size:14px;color:#333}
.top-tab{position:absolute;top:0;height:30px;color:#fff;font-size:14px;display:flex;align-items:center;justify-content:center}
.tab-login{left:815px;width:88px;background:var(--red);clip-path:polygon(10% 0,100% 0,100% 100%,0 100%)}
.tab-phone{left:903px;width:170px;background:var(--blue);font-weight:600;clip-path:polygon(0 0,100% 0,92% 100%,0 100%)}

/* hero */
.hero{position:absolute;left:0;top:87px;width:1200px;height:730px;background:linear-gradient(180deg,#3a3f48 0%,#4d4a45 45%,#5a4f42 100%)}
.hero-shade{position:absolute;inset:0;background:rgba(20,22,30,.45)}
.badge-welcome{position:absolute;left:530px;top:300px;width:163px;height:35px;background:var(--red);color:#fff;font-size:11px;font-weight:700;display:flex;align-items:center;justify-content:center;letter-spacing:.5px}
.hero-title{position:absolute;left:0;top:350px;width:1225px;text-align:center;color:#fff;font-size:61px;font-weight:700;line-height:70px;letter-spacing:1px}
.btn-outline{position:absolute;left:528px;top:517px;width:168px;height:47px;border:1.5px solid #fff;color:#fff;font-size:11px;font-weight:700;display:flex;align-items:center;justify-content:center}

/* labels */
.eyebrow{position:absolute;font-size:12px;color:var(--red);border-bottom:1px solid var(--red);padding-bottom:2px;text-transform:uppercase}
.section-title{position:absolute;font-size:42px;font-weight:500;color:var(--navy)}
.section-title em{font-style:normal;color:var(--red)}

/* about */
.about-title{left:619px;top:950px;font-size:38px;line-height:46px;font-weight:500;color:var(--navy)}
.about-sub{position:absolute;left:619px;top:1070px;font-size:19px;color:#222}
.about-copy{position:absolute;left:619px;width:455px;font-size:12px;line-height:20px;color:var(--muted)}
.btn-red{position:absolute;background:var(--red);color:#fff;font-size:14px;font-weight:600;display:flex;align-items:center;justify-content:center;gap:14px}

/* services */
.services-bg{position:absolute;left:0;top:1500px;width:1200px;height:588px;background:var(--light)}
.service-card{position:absolute;top:1780px;width:304px;height:215px;background:#fff;box-shadow:0 4px 14px rgba(0,0,0,.06);text-align:center}
.service-card h3{margin-top:112px;font-size:18px;font-weight:500;color:var(--navy)}
.service-card p{margin:4px auto 0;width:230px;font-size:13px;line-height:20px;color:var(--muted)}
.service-photo{position:absolute;top:1710px;width:150px;height:150px;border-radius:50%;border:6px solid #e8ebf2}
.num{position:absolute;top:1845px;width:30px;height:30px;border-radius:50%;background:var(--red);color:#fff;font-size:12px;font-weight:700;display:flex;align-items:center;justify-content:center}

/* call band */
.call-band{position:absolute;left:0;top:2088px;width:1200px;height:305px;background:linear-gradient(90deg,#1f2126,#3a3b40 50%,#26282d)}
.call-title{position:absolute;left:0;top:2198px;width:1212px;text-align:center;color:#fff;font-size:33px;line-height:40px}
.call-title em{font-style:normal;color:var(--red)}
.contact-strip{position:absolute;left:350px;top:2363px;width:500px;height:57px;background:#fff;box-shadow:0 6px 16px rgba(0,0,0,.12);display:flex;align-items:center;justify-content:space-around;font-size:16px;color:#222}

/* faq */
.faq-item{position:absolute;left:610px;width:473px;height:57px;background:var(--light);display:flex;align-items:center;justify-content:space-between;padding:0 12px 0 25px;font-size:14px;font-weight:600;color:var(--navy)}
.faq-item.open{background:var(--red);color:#fff}
.faq-toggle{width:30px;height:30px;background:#fff;color:var(--ink);display:flex;align-items:center;justify-content:center;font-size:14px}
.faq-answer{position:absolute;left:636px;top:2684px;width:440px;font-size:13px;line-height:28px;color:#444}

/* testimonials */
.testi-bg{position:absolute;left:0;top:3000px;width:1200px;height:680px;background:var(--light)}
.quote{position:absolute;top:3298px;width:306px;height:172px;background:#fff;padding:28px 20px;font-size:15px;line-height:23px;color:#333;box-shadow:0 4px 14px rgba(0,0,0,.05)}
.quote.featured{background:var(--red);color:#fff}
.quote-tail{position:absolute;top:3470px;width:0;height:0;border-top:18px solid var(--red);border-right:18px solid transparent}
.person{position:absolute;top:3497px;display:flex;align-items:center;gap:20px}
.avatar{width:52px;height:52px;border-radius:50%;border:3px solid #fff;box-shadow:0 2px 6px rgba(0,0,0,.15)}
.person b{display:block;font-size:14px;font-weight:600;color:#111}
.person span{font-size:13px;color:var(--muted)}

/* footer */
.footer{position:absolute;left:0;top:3640px;width:1200px;height:609px;background:var(--footer);color:#c9c6d6}
.f-brand{position:absolute;left:128px;top:3790px;font-size:30px;font-weight:700;color:#fff;display:flex;align-items:center;gap:10px}
.f-brand .dot{width:22px;height:22px;border-radius:50%;background:var(--red)}
.f-text{position:absolute;font-size:12px;line-height:22px;color:#c9c6d6}
.f-head{position:absolute;font-size:14px;font-weight:700;color:#fff}
.f-links{position:absolute;font-size:12px;line-height:26px;color:#c9c6d6;list-style:none}
.social{position:absolute;top:3950px;width:30px;height:30px;background:#3a3450}
.social.on{background:var(--red)}
.news-input{position:absolute;left:827px;top:3911px;width:197px;height:47px;background:#fff;font-size:12px;color:#777;display:flex;align-items:center;padding-left:24px}
.news-btn{position:absolute;left:1024px;top:3911px;width:47px;height:47px;background:var(--red);display:flex;align-items:center;justify-content:center}
.info{position:absolute;top:4065px;display:flex;align-items:center;gap:14px}
.info .ico{width:48px;height:48px;border-radius:50%;background:#3a3450;display:flex;align-items:center;justify-content:center}
.info .ico.red{background:var(--red)}
.info b{display:block;font-size:15px;color:#fff;font-family:"Ubuntu",sans-serif;font-weight:500}
.info span{font-size:12px;color:#c9c6d6}
.f-rule{position:absolute;left:128px;top:4195px;width:944px;height:1px;background:#3a3450}
.copyright{position:absolute;left:0;top:4210px;width:1212px;text-align:center;font-size:12px;color:#fff}
</style>
</head>
<body>

<header class="site-header">
  <div class="brand"><span class="dot"></span>TRL Vetting</div>
  <a class="nav" style="left:518px">Home</a>
  <a class="nav" style="left:612px">About Us</a>
  <a class="nav" style="left:707px">Services</a>
  <a class="nav" style="left:807px">Contact Us</a>
  <a class="nav" style="left:922px">FAQ</a>
</header>
<div class="top-tab tab-login" style="z-index:4">Log in</div>
<div class="top-tab tab-phone" style="z-index:4">+1 (555) 010-2740</div>

<section class="hero" role="img" aria-label="Business team meeting around a table in a bright office">
  <div class="hero-shade"></div>
</section>
<div class="badge-welcome">WELCOME</div>
<h1 class="hero-title">Reliable Insights for<br>Confident Decisions</h1>
<div class="btn-outline">ABOUT COMPANY</div>
<svg class="abs" style="left:0;top:720px" width="1200" height="100" viewBox="0 0 1200 100">
  <path d="M0 100 Q600 -10 1200 100 Z" fill="#fff"/>
  <path d="M110 75 Q600 -20 1090 75 Q600 15 110 75 Z" fill="#c0192c"/>
</svg>

<!-- about -->
<div class="photo" style="left:145px;top:962px;width:173px;height:218px;background:linear-gradient(160deg,#d8d3cc,#7a6a5e)" role="img" aria-label="Smiling woman working at a laptop"></div>
<div class="photo" style="left:340px;top:878px;width:233px;height:302px;background:linear-gradient(160deg,#9bb6c9,#3d5c7a)" role="img" aria-label="Two colleagues laughing by a window"></div>
<div class="photo" style="left:197px;top:1196px;width:140px;height:141px;background:linear-gradient(160deg,#cfd4d9,#5d6670)" role="img" aria-label="Man reviewing documents at a computer desk"></div>
<div class="photo" style="left:358px;top:1196px;width:184px;height:169px;background:linear-gradient(160deg,#b9c3cc,#3e4856)" role="img" aria-label="Businessman using a tablet at a desk"></div>
<div class="eyebrow" style="left:619px;top:918px">Who we are</div>
<h2 class="section-title about-title">Reliable Insights for<br>Confident Decisions</h2>
<div class="about-sub">Confidence Starts with a Clear Background</div>
<p class="about-copy" style="top:1108px">Lorem ipsum dolor sit amet, consectetur adipiscing elit, sed do eiusmod temp or incididunt ut labore et dolore magna aliqua. Ut enim ad minim veniam, quis laboris nisi ut aliquip ex ea commodo consequat.</p>
<p class="about-copy" style="top:1176px">Lorem ipsum dolor sit amet, consectetur adipiscing elit, sed do eiusmod temp or incididunt ut labore et dolore magna aliqua.</p>
<div class="btn-red" style="left:619px;top:1241px;width:137px;height:40px">Contact us
  <svg width="16" height="12" viewBox="0 0 16 12"><path d="M0 6h14M9 1l5 5-5 5" stroke="#fff" stroke-width="1.6" fill="none"/></svg>
</div>

<!-- services -->
<div class="services-bg"></div>
<svg class="abs" style="left:0;top:1455px" width="1200" height="95" viewBox="0 0 1200 95">
  <path d="M0 0 H1200 V95 Q600 -5 0 95 Z" fill="#fff"/>
  <path d="M115 62 Q600 -35 1085 62 Q600 -12 115 62 Z" fill="#c0192c"/>
</svg>
<div class="eyebrow" style="left:537px;top:1566px">Our services</div>
<h2 class="section-title" style="left:383px;top:1602px">Services We <em>Provide</em></h2>

<div class="service-card" style="left:119px"><h3>County Criminal</h3><p>Lorem ipsum dolor sit amet, consect etur adipiscing elit, sed do eiu smod tempor</p></div>
<div class="service-card" style="left:447px"><h3>Public Records</h3><p>Lorem ipsum dolor sit amet, consect etur adipiscing elit, sed do eiu smod tempor</p></div>
<div class="service-card" style="left:776px"><h3>Employment Screen</h3><p>Lorem ipsum dolor sit amet, consect etur adipiscing elit, sed do eiu smod tempor</p></div>
<div class="service-photo" style="left:196px;background:linear-gradient(160deg,#d9dde2,#3b4452)" role="img" aria-label="Businessman in a suit in an office"></div>
<div class="service-photo" style="left:524px;background:linear-gradient(160deg,#e5e5e5,#2a2a2a)" role="img" aria-label="Professional woman holding a tablet"></div>
<div class="service-photo" style="left:853px;background:linear-gradient(160deg,#c8ccd2,#4a4f58)" role="img" aria-label="Colleagues reviewing documents together"></div>
<div class="num" style="left:257px">01</div>
<div class="num" style="left:585px">02</div>
<div class="num" style="left:914px">03</div>

<!-- call band -->
<section class="call-band" role="img" aria-label="Dim office with people working, darkened backdrop"></section>
<h2 class="call-title">We're On <em>Call 24/7</em> to React Promptly to Your<br>Background Checks Needs</h2>
<div class="contact-strip"><span>+ (001) 555-010-274</span><span>[or]</span><span>info@trlvetting.example</span></div>

<!-- faq -->
<svg class="abs" style="left:137px;top:2553px" width="375" height="375" viewBox="0 0 375 375">
  <circle cx="175" cy="180" r="175" fill="#c0192c"/>
  <circle cx="200" cy="195" r="175" fill="#13285e"/>
</svg>
<div class="photo" style="left:152px;top:2568px;width:345px;height:345px;border-radius:50%;background:linear-gradient(160deg,#e4e2e0,#8a8380)" role="img" aria-label="Woman with glasses working at a desk"></div>
<div class="eyebrow" style="left:610px;top:2497px">FAQs</div>
<h2 class="section-title" style="left:610px;top:2533px;font-size:36px">Frequently Asked <em>Questions</em></h2>
<div class="faq-item open" style="top:2601px">How to Get Started with our Programs<span class="faq-toggle">–</span></div>
<p class="faq-answer">Lorem ipsum dolor sit amet, consectetur adipiscing elit, sed do eiusmod tempor incididunt ut labore et dolore magna aliqua. Ut enim ad minim veniam, enim ad minim veniam,</p>
<div class="faq-item" style="top:2797px">How to Get Started with our Programs<span class="faq-toggle">+</span></div>
<div class="faq-item" style="top:2862px">How to Get Started with our Programs<span class="faq-toggle">+</span></div>

<!-- testimonials -->
<div class="testi-bg"></div>
<svg class="abs" style="left:0;top:3000px" width="1200" height="90" viewBox="0 0 1200 90">
  <path d="M0 0 H1200 Q600 95 0 0 Z" fill="#fff"/>
  <path d="M115 27 Q600 110 1085 27 Q600 80 115 27 Z" fill="#c0192c"/>
</svg>
<div class="eyebrow" style="left:557px;top:3164px">Testimonials</div>
<h2 class="section-title" style="left:366px;top:3196px">What Clients are <em>Saying</em></h2>

<div class="quote" style="left:119px">Lorem ipsum dolor sit amet, consectetur adipiscing elit, sed d o eiusmod tempor incididunt ut lab ore et dolore magna aliqua. Ut enim ad min</div>
<div class="quote featured" style="left:447px">Lorem ipsum dolor sit amet, consectetur adipiscing elit, sed d o eiusmod tempor incididunt ut lab ore et dolore magna aliqua. Ut enim ad min</div>
<div class="quote" style="left:777px">Lorem ipsum dolor sit amet, consectetur adipiscing elit, sed d o eiusmod tempor incididunt ut lab ore et dolore magna aliqua. Ut enim ad min</div>
<div class="quote-tail" style="left:119px"></div>
<div class="quote-tail" style="left:447px"></div>
<div class="quote-tail" style="left:777px"></div>
<div class="person" style="left:140px"><div class="avatar" style="background:#5b6b7a" role="img" aria-label="Client portrait"></div><div><b>Dana Whitfield</b><span>Engineer</span></div></div>
<div class="person" style="left:468px"><div class="avatar" style="background:#8a8f96" role="img" aria-label="Client portrait"></div><div><b>Dana Whitfield</b><span>Engineer</span></div></div>
<div class="person" style="left:798px"><div class="avatar" style="background:#7c6f66" role="img" aria-label="Client portrait"></div><div><b>Dana Whitfield</b><span>Engineer</span></div></div>
<svg class="abs" style="left:570px;top:3594px" width="62" height="12" viewBox="0 0 62 12">
  <rect x="0" y="2" width="22" height="8" rx="4" fill="#c0192c"/>
  <circle cx="31" cy="6" r="4" fill="#c0192c"/><circle cx="44" cy="6" r="4" fill="#c0192c"/><circle cx="57" cy="6" r="4" fill="#c0192c"/>
</svg>

<!-- footer -->
<footer class="footer"></footer>
<svg class="abs" style="left:0;top:3630px" width="1200" height="100" viewBox="0 0 1200 100">
  <path d="M0 0 H1200 V10 Q600 130 0 10 Z" fill="#f3f5fa"/>
  <path d="M115 33 Q600 118 1085 33 Q600 92 115 33 Z" fill="#c0192c"/>
</svg>
<div class="f-brand brand"><span class="dot"></span>TRL Vetting</div>
<p class="f-text" style="left:126px;top:3884px;width:290px">Lorem ipsum dolor sit amet, consectetur adipiscing elit, sed do eiusmod tempor incididunt ut</p>
<div class="social on" style="left:128px"></div>
<div class="social" style="left:166px"></div>
<div class="social" style="left:204px"></div>
<div class="social" style="left:242px"></div>

<div class="f-head" style="left:490px;top:3812px">Quick Links</div>
<ul class="f-links" style="left:490px;top:3853px"><li>Lorest Services</li><li>Lorest Services</li><li>Lorest Services</li><li>Lorest Services</li><li>Lorest Services</li><li>Lorest Services</li></ul>
<ul class="f-links" style="left:626px;top:3853px"><li>Lorest Services</li><li>Lorest Services</li><li>Lorest Services</li><li>Lorest Services</li><li>Lorest Services</li></ul>

<div class="f-head" style="left:827px;top:3812px">Newsletters</div>
<p class="f-text" style="left:827px;top:3850px;width:250px">Lorem ipsum dolor sit amet, consectetur adi piscing elit, sed do eiusmod tempor</p>
<div class="news-input">Enter Email Address</div>
<div class="news-btn"><svg width="14" height="18" viewBox="0 0 14 18"><path d="M3 2l7 7-7 7" stroke="#fff" stroke-width="3" fill="none"/></svg></div>

<div class="info" style="left:126px">
  <div class="ico"><svg width="18" height="22" viewBox="0 0 18 22"><path d="M9 1a7 7 0 0 0-7 7c0 5 7 13 7 13s7-8 7-13a7 7 0 0 0-7-7z" fill="#c9c6d6"/><circle cx="9" cy="8" r="2.6" fill="#3a3450"/></svg></div>
  <div><b>Address</b><span>48 Harbor Lane</span></div>
</div>
<div class="info" style="left:365px">
  <div class="ico red"><svg width="20" height="14" viewBox="0 0 20 14"><rect x="1" y="1" width="18" height="12" fill="none" stroke="#fff" stroke-width="1.6"/><path d="M1 1l9 7 9-7" stroke="#fff" stroke-width="1.6" fill="none"/></svg></div>
  <div><b>Email Us</b><span>support@trlvetting.example</span></div>
</div>
<div class="info" style="left:632px">
  <div class="ico"><svg width="20" height="20" viewBox="0 0 24 24"><path d="M6.6 10.8a15 15 0 0 0 6.6 6.6l2.2-2.2c.3-.3.7-.4 1-.2 1.1.4 2.3.6 3.6.6.6 0 1 .4 1 1V20c0 .6-.4 1-1 1C10.6 21 3 13.4 3 4c0-.6.4-1 1-1h3.5c.6 0 1 .4 1 1 0 1.3.2 2.5.6 3.6.1.3 0 .7-.2 1z" fill="#c9c6d6"/></svg></div>
  <div><b>Contact Us</b><span>+012 (555) 010 27</span></div>
</div>
<div class="info" style="left:860px">
  <div class="ico"><svg width="22" height="22" viewBox="0 0 22 22"><circle cx="11" cy="11" r="9" fill="none" stroke="#c9c6d6" stroke-width="1.8"/><path d="M11 6v5l3 2" stroke="#c9c6d6" stroke-width="1.8" fill="none"/></svg></div>
  <div><b>Opening Hour</b><span>Mon - Friday 10 am - 8pm</span></div>
</div>
<div class="f-rule"></div>
<div class="copyright">TRL Vetting</div>

</body>
</html>
```